Healthy lifestyle Influencer business card

I need your creativity to have a business card that I can leave in all the restaurants, hotels and spas I visit to inform them that I am an influencer specializing in the wellness sector and that I will write a review about them. You can use my instagram photos Velusport72 or on my website www.piattileggerinuovi.it. I would like my business card to impress with its creativity! thank you very much!

Contact Information for Business Card

siteweb, instagram, phone number

Font styles to use
Decorative
Script

Colors
0094D4
00A9DD
6FCCEA
C7EBF8
E9F6FB
59FF00
82FF00
B8FF75
E3FFCB
F4FFEA
FFC000
F8CF3A
FAE287
FDF2CF
FEFAEE
F0912C
F2A743
F7CA91
FBE8D2
FDF5EE
EE7325
F08F49
F5BC92
FAE3D3
FDF4ED
EB3D1F
EC4F4E
F09395
F8D3D4
FCEDEE
E54698
E96AAD
F1A4CE
F9D9EA
FCEFF6

Requirements
Nice to have
• creativity

```html
<!DOCTYPE html>
<html lang="it">
<head>
<meta charset="utf-8">
<title>Lieve Tavola – Biglietto da visita</title>
<link href="https://fonts.googleapis.com/css2?family=Montserrat:wght@400;500;600&display=swap" rel="stylesheet">
<style>
  :root{
    --bg:#8a8a88;
    --paper:#fbfbf9;
    --ink:#3d3d3d;
    --orange:#f0912c;
    --orange-soft:#f2a743;
    --cocoa-dark:#3a2a26;
    --cocoa-mid:#5b3f38;
    --cocoa-light:#8c6a60;
    --cream:#ffffff;
  }
  *{box-sizing:border-box;margin:0;padding:0}
  html,body{width:1200px;height:801px;overflow:hidden}
  body{
    background:var(--bg);
    font-family:"Montserrat",sans-serif;
    display:flex;align-items:center;justify-content:center;gap:48px;
  }
  .card{
    width:540px;height:310px;position:relative;
    border-bottom:3px solid var(--orange);
    box-shadow:0 10px 26px rgba(0,0,0,.28);
    overflow:hidden;
  }
  /* Front */
  .card--front{background:var(--paper);color:var(--ink)}
  .brand{position:absolute;right:44px;top:50px;text-align:right}
  .brand__mark{display:flex;align-items:center;gap:10px;justify-content:flex-end}
  .brand__dot{width:12px;height:12px;border-radius:50%;background:var(--orange-soft)}
  .brand__name{font-weight:500;font-size:30px;letter-spacing:.5px;color:var(--ink)}
  .brand__tagline{font-size:10px;margin-top:4px;color:var(--ink)}
  .divider{position:absolute;left:36px;right:36px;top:150px;height:1px;background:var(--orange)}
  .person{position:absolute;left:40px;top:168px}
  .person__name{font-weight:600;font-size:20px;color:var(--orange);letter-spacing:.5px}
  .person__role{font-size:13px;margin-top:2px}
  .contacts{position:absolute;left:40px;top:222px;list-style:none;font-size:12.5px;line-height:19px}
  .contacts li{display:flex;align-items:center;gap:8px}
  .contacts svg{width:11px;height:11px;flex:none}
  /* Back */
  .card--back{color:var(--cream);display:flex;flex-direction:column;align-items:center;justify-content:center}
  .photo{
    position:absolute;inset:0;
    background:radial-gradient(ellipse at 45% 60%, var(--cocoa-light) 0%, var(--cocoa-mid) 40%, var(--cocoa-dark) 100%);
  }
  .back__name{position:relative;font-weight:500;font-size:44px;letter-spacing:1px}
  .back__tagline{position:relative;font-size:17px;margin-top:10px;letter-spacing:.5px}
</style>
</head>
<body>
  <section class="card card--front">
    <div class="brand">
      <div class="brand__mark"><span class="brand__dot"></span><span class="brand__name">Lieve Tavola</span></div>
      <p class="brand__tagline">gusto sano ogni giorno</p>
    </div>
    <div class="divider"></div>
    <div class="person">
      <p class="person__name">MARCO LENTINI</p>
      <p class="person__role">President</p>
    </div>
    <ul class="contacts">
      <li><svg viewBox="0 0 12 12"><path d="M3 1l2 2.2-1 1.3a6 6 0 0 0 3.5 3.5l1.3-1L11 9l-1.2 1.8C5.5 11 1 6.5 1.2 2.2z" fill="var(--orange)"/></svg>321 654 9870</li>
      <li><svg viewBox="0 0 12 12"><circle cx="6" cy="6" r="5" fill="var(--orange)"/></svg>@velusport72</li>
      <li><svg viewBox="0 0 12 12"><rect x="1" y="2.5" width="10" height="7" rx="1" fill="var(--orange)"/><path d="M1.5 3l4.5 3.5L10.5 3" stroke="#fff" stroke-width="1" fill="none"/></svg>info@piattileggerinuovi.it</li>
      <li><svg viewBox="0 0 12 12"><circle cx="6" cy="6" r="5" fill="var(--orange)"/><path d="M1 6h10M6 1c-2 3-2 7 0 10M6 1c2 3 2 7 0 10" stroke="#fff" stroke-width=".8" fill="none"/></svg>www.piattileggerinuovi.it</li>
    </ul>
  </section>

  <section class="card card--back">
    <div class="photo" role="img" aria-label="Foto di una torta al cacao con panna su sfondo scuro"></div>
    <p class="back__name">Lieve Tavola</p>
    <p class="back__tagline">Gusto sano ogni giorno</p>
  </section>
</body>
</html>
```